Upgraded look for current product needed

We need an upgraded look of our 40mg Ginkgo Biloba extract product to a higher strength 125mg Ginkgo Biloba extract product to depict a premium look yet retain enough familiarity for our current consumers to be able to recognize it easily. Both products will be on shelves at the same time so it cannot be too similar. Please visit our website to find out more about our company, product range and current product. www.kelvarra.com.my. Need not be too concerned about the text but please leave enough space for it. Our current color is Dark Green with Gold Hot stamping. Other products use Gold or Silver hot stamping.
Updates

Project Deadline Extended
Reason: We are still looking for more options before making a decision.

Industry/Entity Type

Health Product

Requirements
Must have
• Blend in with the rest of the range

```html
<!DOCTYPE html>
<html lang="en">
<head>
<meta charset="utf-8">
<title>Kelvarra Activated Ginkgo Extract 125mg – Pack Front</title>
<link rel="stylesheet" href="https://fonts.googleapis.com/css2?family=Montserrat:wght@700&family=Tinos:wght@700&family=Roboto+Condensed:wght@700&family=Noto+Sans+JP:wght@700&display=swap">
<style>
  :root {
    --gold: #b88e00;
    --leaf-grey: #d9d9d9;
    --rule-grey: #c8c8c8;
    --paper: #ffffff;
    --arch-fill: #f6efd9;
  }
  html, body {
    margin: 0;
    width: 1200px;
    height: 1000px;
    overflow: hidden;
    background: var(--paper);
  }
  .canvas {
    position: relative;
    width: 1200px;
    height: 1000px;
  }
  .pack-front {
    position: absolute;
    left: 434px;
    top: 162px;
    width: 334px;
    height: 334px;
    background: var(--paper);
    overflow: hidden;
  }
  .leaf-pattern {
    position: absolute;
    inset: 9px 0;
    background: linear-gradient(90deg, var(--leaf-grey) 0%, #ececec 30%, #ececec 70%, var(--leaf-grey) 100%);
  }
  .band {
    position: absolute;
    left: 0;
    width: 100%;
    height: 9px;
    background: var(--gold);
  }
  .band--top { top: 0; }
  .band--bottom { bottom: 0; }
  .arch-window {
    position: absolute;
    left: 85px;
    top: 28px;
    width: 167px;
    height: 188px;
  }
  .product-name-jp {
    position: absolute;
    left: 259px;
    top: 38px;
    height: 182px;
    writing-mode: vertical-rl;
    text-orientation: upright;
    font-family: "Noto Sans JP", sans-serif;
    font-weight: 700;
    font-size: 12px;
    line-height: 14px;
    letter-spacing: 0.8px;
    white-space: nowrap;
    color: var(--gold);
  }
  .label-panel {
    position: absolute;
    left: 7px;
    width: 320px;
    background: var(--paper);
    border: 2px solid var(--rule-grey);
    box-sizing: border-box;
    text-align: center;
    color: var(--gold);
  }
  .label-panel--main { top: 226px; height: 67px; }
  .label-panel--count { top: 291px; height: 34px; }
  .brand-name {
    margin: 2px 0 0;
    font-family: "Montserrat", sans-serif;
    font-weight: 700;
    font-size: 38px;
    line-height: 40px;
    letter-spacing: 1px;
  }
  .strength-line {
    margin: 0;
    font-family: "Tinos", serif;
    font-weight: 700;
    font-size: 15px;
    line-height: 20px;
    white-space: nowrap;
  }
  .strength-line .dose { font-size: 21px; }
  .strength-line .unit { font-size: 14px; }
  .tablet-count {
    margin: 0;
    font-family: "Roboto Condensed", sans-serif;
    font-weight: 700;
    font-size: 16px;
    line-height: 30px;
  }
</style>
</head>
<body>
<main class="canvas">
  <section class="pack-front">
    <div class="leaf-pattern" role="img" aria-label="Pale grey ginkgo leaf pattern across the pack background"></div>
    <div class="band band--top"></div>
    <div class="band band--bottom"></div>

    <svg class="arch-window" viewBox="0 0 167 188">
      <path d="M2 186 V82 A81.5 80 0 0 1 165 82 V186 Z" fill="var(--paper)" stroke="var(--gold)" stroke-width="3"/>
      <path d="M8 180 V84 A75.5 74 0 0 1 159 84 V180 Z" fill="var(--arch-fill)" role="img" aria-label="Gold ginkgo branch illustration"/>
    </svg>

    <div class="product-name-jp">ケルバラ活性イチョウ葉エキス</div>

    <div class="label-panel label-panel--main">
      <p class="brand-name">kelvarra</p>
      <p class="strength-line">ACTIVATED GINKGO EXTRACT <span class="dose">125</span><span class="unit">mg</span></p>
    </div>
    <div class="label-panel label-panel--count">
      <p class="tablet-count">30 Tablets</p>
    </div>
  </section>
</main>
</body>
</html>
```